Business Cards and Stationery for CPA Firm
Gallowen & Company, P.C.
Business Cards and Stationery for CPA Firm -
Creative Brief
Professional
Bennett L. Gallowen
P.O. Box 482 9 West Cedar Ave. Harrowfield, ST 00000
bgallowen@gallowencpa-example.com
www.gallowencpa-example.com
Need business cards and stationery for a CPA firm. I am open to design ideas and will provide feedback. Our generic email address for letterhead/fax is info@gallowencpa-example.com. This should be used in all locations except the business card. Each person with a business card will have his/her own email address.
Day - I've seen some with checkboxes for day of week. Other ideas welcome. Date Time Note

```html
<!DOCTYPE html>
<html lang="en">
<head>
<meta charset="utf-8">
<title>Gallowen &amp; Company, P.C. — Stationery</title>
<link rel="stylesheet" href="https://fonts.googleapis.com/css2?family=Open+Sans:wght@400;600&display=swap">
<style>
:root{
  --board:#8b8c8e;
  --board-light:#a3a4a6;
  --paper:#ffffff;
  --blue:#1e55c9;
  --blue-deep:#0a2766;
  --navy:#17284d;
  --ink:#3b3f47;
  --rule:#c9ccd2;
}
*{box-sizing:border-box;margin:0;padding:0}
html,body{width:1200px;height:626px;overflow:hidden}
body{font-family:"Open Sans",sans-serif;color:var(--ink);
  background:radial-gradient(ellipse at 55% 45%,var(--board-light),var(--board) 75%);position:relative}
.sheet{position:absolute;background:var(--paper);box-shadow:0 2px 6px rgba(0,0,0,.35)}
.band{position:absolute;left:0;top:0;bottom:0;background:linear-gradient(90deg,var(--blue-deep),var(--blue) 55%,#6f95e6)}
.brand{position:absolute;display:flex;align-items:center;gap:6px}
.brand-mark{background:var(--navy);flex:none}
.brand-name{font-family:"Open Sans",sans-serif;font-weight:600;color:var(--navy);white-space:nowrap;line-height:1.1}
.brand-tag{font-family:"Open Sans",sans-serif;font-weight:400;color:var(--ink);white-space:nowrap;margin-top:2px}
.small{font-size:5px;line-height:1.5;color:var(--ink)}
.appt{left:34px;top:206px;width:182px;height:108px;padding:10px 12px}
.appt .line{border-bottom:1px solid var(--rule);height:9px;margin-bottom:4px;font-size:5px}
.appt .days{display:flex;gap:7px;font-size:5px;margin:6px 0}
.appt .days span::before{content:"";display:inline-block;width:5px;height:5px;border:1px solid #888;margin-right:2px;vertical-align:-1px}
.card{left:34px;top:326px;width:182px;height:108px}
.letter{left:230px;top:24px;width:430px;height:588px}
.letter-foot{position:absolute;left:44px;right:30px;bottom:22px;display:flex;justify-content:space-between;font-size:5.5px;line-height:1.5}
.env-back{left:679px;top:79px;width:492px;height:233px;overflow:hidden}
.env-front{left:679px;top:336px;width:492px;height:240px}
.env-return{position:absolute;left:44px;top:80px;font-size:4.5px;line-height:1.5;display:flex;gap:40px}
</style>
</head>
<body>

<section class="sheet appt" aria-label="Appointment card back">
  <div class="line">Appointment for</div>
  <div class="line"></div>
  <div class="days"><span>M</span><span>T</span><span>W</span><span>T</span><span>F</span></div>
  <div class="line">Date</div>
  <div class="line">Time</div>
</section>

<section class="sheet card" aria-label="Business card front">
  <div class="band" style="width:10px"></div>
  <div class="brand" style="left:16px;top:14px">
    <div class="brand-mark" style="width:11px;height:11px"></div>
    <div><div class="brand-name" style="font-size:10px">Gallowen &amp; Company, P.C.</div>
    <div class="brand-tag" style="font-size:4.5px">Certified Public Accountants</div></div>
  </div>
  <div class="small" style="position:absolute;left:16px;top:52px">
    <strong style="font-size:6px">Bennett L. Gallowen</strong><br>Certified Public Accountant
  </div>
  <div class="small" style="position:absolute;left:16px;top:78px">
    P.O. Box 482 9 West Cedar Ave. Harrowfield, ST 00000<br>bgallowen@gallowencpa-example.com<br>(555) 555-0142
  </div>
</section>

<section class="sheet letter" aria-label="Letterhead">
  <div class="band" style="width:26px"></div>
  <div class="brand" style="left:34px;top:16px">
    <div class="brand-mark" style="width:16px;height:16px"></div>
    <div><div class="brand-name" style="font-size:15px">Gallowen &amp; Company, P.C.</div>
    <div class="brand-tag" style="font-size:6px">Certified Public Accountants</div></div>
  </div>
  <div class="letter-foot">
    <div>P (555) 555-0142<br>F (555) 555-0143<br>info@gallowencpa-example.com</div>
    <div>www.gallowencpa-example.com</div>
    <div>P.O. Box 482<br>9 West Cedar Ave.<br>Harrowfield, ST 00000</div>
  </div>
</section>

<section class="sheet env-back" aria-label="Envelope back">
  <svg width="492" height="233" viewBox="0 0 492 233" aria-hidden="true">
    <defs>
      <radialGradient id="flapGlow" cx="50%" cy="10%" r="65%">
        <stop offset="0" stop-color="#2f6ae0"/><stop offset="1" stop-color="#0a2766"/>
      </radialGradient>
    </defs>
    <path d="M0 0H492V30Q246 120 0 30Z" fill="url(#flapGlow)"/>
  </svg>
</section>

<section class="sheet env-front" aria-label="Envelope front">
  <div class="band" style="width:12px"></div>
  <div class="brand" style="left:22px;top:14px">
    <div class="brand-mark" style="width:15px;height:15px"></div>
    <div><div class="brand-name" style="font-size:14px">Gallowen &amp; Company, P.C.</div>
    <div class="brand-tag" style="font-size:5.5px">Certified Public Accountants</div></div>
  </div>
  <div class="env-return">
    <div>P (555) 555-0142<br>F (555) 555-0143</div>
    <div>info@gallowencpa-example.com<br>www.gallowencpa-example.com</div>
    <div>P.O. Box 482 9 West Cedar Ave.<br>Harrowfield, ST 00000</div>
  </div>
</section>

</body>
</html>
```